Etiketten für Honig
Zielgruppe
Es scheint Missverständnisse zu geben weshalb ich das Briefing wohl ändern muss.
see below for English translation
Wir sind eine kleine Imkerei, die von der Liebhaberei in den Nebenerwerb wechselt. Wir verkaufen verschiedene Sortenhonige und Honigzubereitungen (siehe Webseite) im vorwiegend ländlichen Raum des Münsterlandes.
Entsprechend unseres Standortes und unserer Kundschaft benötigen wir ein klassisch ländliches Design. Hierfür haben wir auch bereits ein Logo welches verwendet werden muss.
English
There seems to be some misunderstanding, so I guess I'll have to change the briefing.
We are a small apiary that changes from hobby to sideline. We sell different types of honey and honey preparations (e.g. honey with raspberry) in a predominantly rural area of the Münsterland (Muensterland).
According to our location and our clientele, we need a classic rural design. We already have a logo which must be used.
Aufgabenstellung
Wir möchten ein rechteckiges Etikett mit Gewährverschluss das für verschiedene Sorten adoptierbar ist. Zum Beispiel durch den Austausch der Sortenbezeichnung und eine farbliche Veränderung.
Das Design soll später auf Naturpapier oder Graspapier gedruckt werden. Das Logo muss auf Etikett und Gewährverschluss abgebildet werden.
We would like a rectangular label with a guarantee seal that is adoptable for different varieties. For example, by exchanging the variety designation and changing the color.
The design will later be printed on uncoated paper or grass paper. The logo must be shown on the label and guarantee seal.

```html
<!DOCTYPE html>
<html lang="de">
<head>
<meta charset="utf-8">
<title>Etikett Sommertracht – Honigwerk Marlen</title>
<link rel="stylesheet" href="https://fonts.googleapis.com/css2?family=Montserrat:wght@500;600;700&family=Kaushan+Script&family=Caveat+Brush&display=swap">
<style>
  :root {
    --teal: #0b5456;
    --honey: #f0b323;
    --honey-pale: #f6d473;
    --white: #ffffff;
    --ink: #111111;
  }
  html, body {
    margin: 0;
    padding: 0;
    overflow: hidden;
    background: var(--white);
  }
  .canvas {
    position: relative;
    width: 1061px;
    height: 1200px;
    overflow: hidden;
    background: var(--white);
    font-family: "Montserrat", sans-serif;
  }
  .seal {
    position: absolute;
    left: 0;
    top: 0;
  }
  .seal-name {
    position: absolute;
    left: 406px;
    top: 168px;
    width: 290px;
    text-align: center;
    font-family: "Montserrat", sans-serif;
    font-weight: 700;
    font-size: 24px;
    line-height: 1.2;
    color: var(--teal);
  }
  .label-band {
    position: absolute;
    left: 0;
    top: 772px;
    width: 1061px;
    height: 428px;
    background: var(--teal);
  }
  .maker {
    position: absolute;
    left: 25px;
    top: 30px;
    width: 260px;
    color: var(--honey);
  }
  .maker-name {
    display: flex;
    align-items: center;
    gap: 8px;
    margin: 0 0 12px;
    font-family: "Montserrat", sans-serif;
    font-weight: 700;
    font-size: 22px;
  }
  .maker-name::before {
    content: "";
    width: 14px;
    height: 14px;
    border-radius: 50%;
    background: var(--honey);
  }
  .maker-address {
    margin: 0;
    font-style: normal;
    font-size: 13.5px;
    font-weight: 500;
    line-height: 1.28;
  }
  .storage {
    position: absolute;
    left: 25px;
    top: 228px;
    width: 260px;
    color: var(--honey);
    font-size: 13.5px;
    font-weight: 500;
    line-height: 1.28;
  }
  .storage-origin {
    margin: 0;
    font-family: "Kaushan Script", cursive;
    font-size: 17px;
    font-weight: 400;
  }
  .storage-note { margin: 0; }
  .storage-glass { margin: 10px 0 0; }
  .best-before {
    position: absolute;
    left: 21px;
    top: 321px;
    width: 195px;
    height: 80px;
    background: var(--white);
    box-sizing: border-box;
    padding: 6px 6px;
    font-size: 10.5px;
    font-weight: 600;
    color: var(--ink);
  }
  .variety {
    position: absolute;
    left: 300px;
    top: 62px;
    width: 520px;
  }
  .variety-origin {
    margin: 0 0 0 72px;
    font-weight: 600;
    font-size: 23px;
    letter-spacing: 0.3px;
    color: var(--honey);
  }
  .variety-name {
    margin: 0;
    font-family: "Caveat Brush", cursive;
    font-weight: 400;
    line-height: 0.8;
  }
  .variety-name .season {
    display: block;
    font-size: 138px;
    color: var(--white);
    letter-spacing: 4px;
  }
  .variety-name .flow {
    display: block;
    margin-left: 55px;
    font-size: 138px;
    color: var(--honey-pale);
  }
  .claim {
    position: absolute;
    left: 420px;
    top: 316px;
    width: 200px;
    margin: 0;
    font-family: "Kaushan Script", cursive;
    font-size: 17px;
    line-height: 1.15;
    text-align: center;
    color: var(--honey);
    transform: rotate(-7deg);
  }
  .weight {
    position: absolute;
    left: 612px;
    top: 303px;
  }
</style>
</head>
<body>
<main class="canvas">

  <svg class="seal" width="1061" height="780" viewBox="0 0 1061 780" aria-hidden="true">
    <rect class="seal-stem" x="468" y="330" width="120" height="450" fill="var(--teal)"/>
    <circle class="seal-ring" cx="551" cy="186" r="172" fill="var(--teal)"/>
    <circle class="seal-face" cx="551" cy="186" r="145" fill="var(--white)"/>
  </svg>
  <p class="seal-name">Honigwerk<br>Marlen</p>

  <section class="label-band">
    <div class="maker">
      <p class="maker-name">Honigwerk Marlen</p>
      <address class="maker-address">
        Lindenweg 12<br>
        48999 Feldheim<br>
        01234 567890<br>
        honigwerk-marlen.de
      </address>
    </div>

    <div class="storage">
      <p class="storage-origin">Honig aus Deutschland</p>
      <p class="storage-note">Trocken, dunkel und vor<br>Wärme geschützt lagern</p>
      <p class="storage-glass">Mehrwegglas</p>
    </div>

    <div class="best-before">Mindestens haltbar bis:</div>

    <div class="variety">
      <p class="variety-origin">FELDHEIMER LANDHONIG</p>
      <h1 class="variety-name">
        <span class="season">Sommer</span>
        <span class="flow">tracht</span>
      </h1>
    </div>

    <p class="claim">Echter Honig aus<br>dem Münsterland!</p>

    <svg class="weight" width="76" height="80" viewBox="0 0 76 80" aria-label="500 g">
      <polygon points="38,2 72,21 72,59 38,78 4,59 4,21" fill="var(--honey)" transform="rotate(-8 38 40)"/>
      <text x="38" y="47" text-anchor="middle" font-family="Montserrat, sans-serif" font-weight="700" font-size="18" fill="var(--white)" transform="rotate(-20 38 40)">500 g</text>
    </svg>
  </section>

</main>
</body>
</html>
```